Wordpress Powered Website. Outstanding Design Required. Using Morvento Theme

Designers will not need to create anything other than the home page but there are some design elements on the home page which also need to be factored in: 6 product place holders and 2-3 slides for a slideshow (with images I provide).

Designers will need to familiarise themselves with the Morvento theme to make sure that their design will work within the theme.

The winning designer will set up all the pages and navigation in place. This includes social media icons, favicon, widgets, etc. In other words, the home page needs to be designed and coded and the other preset theme pages need to be organised in a way that we can start using the website on completion of the job.

Most of the designs I had last time were too colourful. This needs to be subtle not in your face.

Background to the business/website:
Tallow Banners is a new Australian venture which will sell large format printed banners and other signage. The market is very competitive so it is important to stand out visually and to have a website which is clean, easy to navigate and easy to order. It will be a combination of online sales and assisted sales but all sales enquiries will come from the website.

As our business is focused on presentation it is vital to have excellent design.
Purchased theme is Morvento. Only this theme is to be used.

1. A home page using all the preset features of the Morvento theme - it will just be basically taking my wireframe and inputting it to the live theme.
2. A three slide slideshow, ideally with an edited video. The static image slides can be provided by me during the handover. Placeholder for now.
Similar to this one: http://thebrindlework.com.au/

Attached is the logo which must be utilised, although it could also sit on a dark background. There is our mascot as well which can be used but does not have to be included.

Target Market(s)

Primarily B2B (business to business)
Main industries will be Construction, Retail, Community, Events & Trade Shows

Industry/Entity Type

Printing

Coding

Coded - Design and coding required

Font styles to use
Sans Serif

Requirements
Must have
• Must have the design files made to web pages within the Wordpress environment.
Nice to have
• Clean design. Stand out from competitors based on design.
Should not have
• Should not look like any competitor

```html
<!DOCTYPE html>
<html lang="en">
<head>
<meta charset="utf-8">
<title>Tallow Banners — Home</title>
<link rel="stylesheet" href="https://fonts.googleapis.com/css2?family=Roboto+Condensed:wght@300;400;700&family=Oswald:wght@300;400&display=swap">
<style>
:root{
  --header:#d9ab94;
  --hero-a:#d6dde0;
  --hero-b:#7d919b;
  --products:#d6d4a6;
  --accent-red:#b8624f;
  --card-red:#c5806d;
  --why:#7d8dc2;
  --process:#eeecd0;
  --process-title:#9a7446;
  --teal:#6f9ea8;
  --teal-line:#55848e;
  --works:#b3b294;
  --quote:#7a8bc4;
  --testi:#e8dfae;
  --footer:#6b6b6b;
  --footer-dark:#3b3b3b;
  --white:#ffffff;
  --ink:#2a2a2a;
}
*{box-sizing:border-box;margin:0;padding:0}
html,body{width:1200px;height:4000px;overflow:hidden}
body{position:relative;font-family:"Roboto Condensed",Arial,sans-serif;color:var(--white);background:#fff}
h2{font-weight:400}
.abs{position:absolute}
section,header,footer{position:absolute;left:0;width:1200px}

/* header */
.site-header{top:0;height:137px;background:var(--header)}
.brand{left:74px;top:44px;display:flex;align-items:center;gap:12px}
.brand-mark{width:34px;height:34px;background:var(--white)}
.brand-name{font-size:34px;font-weight:700;color:var(--white);letter-spacing:.5px}
.main-nav a{position:absolute;top:52px;font-size:24px;font-weight:300;color:var(--white);text-decoration:none;letter-spacing:1px}

/* hero */
.hero{top:137px;height:453px}
.hero-media{position:absolute;inset:0;background:linear-gradient(180deg,var(--hero-a) 0%,#e9eef0 45%,var(--hero-b) 100%)}
.slide-arrow{position:absolute;top:322px;width:38px;height:38px;border-radius:50%;background:#111}
.play{position:absolute;left:524px;top:281px;width:140px;height:140px}

/* products */
.products{top:590px;height:881px;background:var(--products)}
.section-title{position:absolute;left:0;width:1200px;text-align:center}
.products .section-title{top:50px;font-size:30px;color:var(--accent-red);letter-spacing:1px}
.product-card{position:absolute;width:302px}
.product-card .media{position:absolute;inset:0}
.product-label{position:absolute;left:0;right:0;bottom:22px;text-align:center;font-size:27px;color:var(--white);text-shadow:0 0 3px #4a557a,0 0 3px #4a557a}

/* why */
.why{top:1471px;height:432px;background:var(--why)}
.why-title{top:38px;font-size:30px}
.why-sub{top:92px;font-size:15px;letter-spacing:.5px}
.feature{position:absolute;top:143px;width:230px;text-align:center}
.feature .icon{width:95px;height:100px;margin:0 auto;display:block}
.feature span{display:block;margin-top:28px;font-size:24px}

/* process */
.process{top:1903px;height:499px;background:var(--process)}
.process .section-title{top:28px;font-size:29px;color:var(--process-title)}
.step{position:absolute;left:78px;width:1049px;background:var(--teal);border-top:3px solid var(--teal-line)}
.step-label{position:absolute;left:44px;font-size:24px}
.step-text{font-size:25px}

/* works */
.works{top:2402px;height:544px;background:var(--works)}
.works .section-title{top:36px;font-size:29px}
.filter{position:absolute;top:98px;font-size:23px}
.filter.active{border:2px solid #5a6f8a;background:#7f95b8;padding:6px 12px;top:90px}
.work{position:absolute;top:182px;width:302px;height:314px}

/* quote */
.get-quote{top:2946px;height:532px;background:var(--quote)}
.get-quote .section-title{top:30px;font-size:34px}
.field-label{position:absolute;font-size:23px}
.field{position:absolute;height:44px;width:302px;background:var(--white)}

/* testimonials */
.testimonials{top:3478px;height:284px;background:var(--testi);color:var(--ink)}
.testimonials .section-title{top:12px;font-family:"Oswald",Arial,sans-serif;font-weight:300;font-size:36px;left:-60px}
.t-box{position:absolute;left:449px;width:602px;background:var(--white);border:2px solid #555;box-shadow:3px 3px 0 #777;font-family:"Oswald",Arial,sans-serif;font-weight:300;font-size:22px;padding:6px 24px}
.t-arrow{position:absolute;top:135px;width:45px;height:42px;background:var(--white)}

/* footer */
.site-footer{top:3762px;height:171px;background:var(--footer);font-size:15px}
.site-footer p{position:absolute;font-size:13px}
.copyright{top:3933px;height:67px;background:var(--footer-dark);text-align:center;font-size:13px;line-height:67px}
</style>
</head>
<body>

<header class="site-header">
  <div class="brand abs"><span class="brand-mark"></span><span class="brand-name">Tallow Banners</span></div>
  <nav class="main-nav">
    <a style="left:594px">PRODUCTS</a>
    <a style="left:776px">GET A QUOTE</a>
    <a style="left:979px">CONTACT US</a>
  </nav>
</header>

<section class="hero">
  <div class="hero-media" role="img" aria-label="Slideshow image: modern shopping centre with a curved banner wrap"></div>
  <svg class="slide-arrow" style="left:149px" viewBox="0 0 38 38"><path d="M23 10 L14 19 L23 28" stroke="#fff" stroke-width="4" fill="none"/></svg>
  <svg class="slide-arrow" style="left:1015px" viewBox="0 0 38 38"><path d="M15 10 L24 19 L15 28" stroke="#fff" stroke-width="4" fill="none"/></svg>
  <svg class="play" viewBox="0 0 140 140"><circle cx="70" cy="70" r="66" fill="#2b2e45" stroke="#d8d8e0" stroke-width="6"/><path d="M52 38 L104 70 L52 102 Z" fill="#fff"/></svg>
</section>

<section class="products">
  <h2 class="section-title">OUR PRODUCTS</h2>
  <div class="product-card" style="left:74px;top:135px;height:313px"><div class="media" role="img" aria-label="Chalet in snowy mountains at night" style="background:linear-gradient(180deg,#7f8fc9,#55639a)"></div><div class="product-label">Banners &amp; Fabrics</div></div>
  <div class="product-card" style="left:450px;top:135px;height:313px"><div class="media" style="background:var(--card-red)"></div><div class="product-label">Boards &amp; Signs</div></div>
  <div class="product-card" style="left:826px;top:132px;height:316px"><div class="media" role="img" aria-label="Racing car on a studio floor" style="background:linear-gradient(180deg,#4a4a4a,#bdbdbd)"></div><div class="product-label">Flags &amp; Posters</div></div>
  <div class="product-card" style="left:74px;top:498px;height:317px"><div class="media" style="background:var(--card-red)"></div><div class="product-label">Self Adhesive vinyles</div></div>
  <div class="product-card" style="left:450px;top:498px;height:317px"><div class="media" role="img" aria-label="Presenter beside a pull-up banner" style="background:linear-gradient(180deg,#333,#6a5450)"></div><div class="product-label">Pullup Banners</div></div>
  <div class="product-card" style="left:826px;top:498px;height:317px"><div class="media" role="img" aria-label="Golden abstract light burst" style="background:radial-gradient(circle at 50% 70%,#c9a45c,#6a4a22 55%,#231a10)"></div><div class="product-label">Posters</div></div>
</section>

<section class="why">
  <h2 class="section-title why-title">Why Tallow Banners ?</h2>
  <p class="section-title why-sub">We could give you hundreds of reasons but let us start with four</p>
  <div class="feature" style="left:101px"><svg class="icon" viewBox="0 0 95 100"><rect width="95" height="100" fill="#eef2e8"/><circle cx="52" cy="36" r="22" fill="#c2d49a"/><rect x="14" y="50" width="60" height="36" fill="#7b9c6c"/></svg><span>Attenssion to Details</span></div>
  <div class="feature" style="left:358px"><svg class="icon" viewBox="0 0 95 100"><rect width="95" height="100" fill="#fff"/><circle cx="47" cy="48" r="34" fill="#d8b471"/><circle cx="47" cy="48" r="26" fill="#fff"/><path d="M47 30 V48 H60" stroke="#333" stroke-width="4" fill="none"/></svg><span>Secured Delivery</span></div>
  <div class="feature" style="left:610px"><svg class="icon" viewBox="0 0 95 100"><rect width="95" height="100" fill="#e2c77a"/><circle cx="47" cy="46" r="26" fill="#4f8790"/><circle cx="47" cy="46" r="10" fill="#e2c77a"/></svg><span>Fast &amp; Flexible</span></div>
  <div class="feature" style="left:861px"><svg class="icon" viewBox="0 0 95 100"><rect width="95" height="100" fill="#fff"/><path d="M30 34 L62 30 L66 66 L34 72 Z" fill="#f2f2f2" stroke="#888" stroke-width="2"/><rect x="32" y="28" width="32" height="10" fill="#d9b060"/></svg><span>Saves Money</span></div>
</section>

<section class="process">
  <h2 class="section-title">Our Process</h2>
  <div class="step" style="top:104px;height:209px">
    <span class="step-label" style="top:6px">Step 1</span>
    <svg class="abs" style="left:14px;top:53px" width="102" height="107" viewBox="0 0 102 107"><rect width="102" height="107" fill="#fff"/><circle cx="51" cy="38" r="20" fill="#222"/><path d="M16 100 Q51 52 86 100 Z" fill="#222"/><path d="M46 62 L51 90 L56 62 Z" fill="#fff"/></svg>
    <span class="abs step-text" style="left:130px;top:88px">Clients send quote</span>
    <svg class="abs" style="left:333px;top:88px" width="48" height="36" viewBox="0 0 48 36"><path d="M2 18 H40 M26 4 L42 18 L26 32" stroke="#222" stroke-width="5" fill="none"/></svg>
    <svg class="abs" style="left:412px;top:17px" width="150" height="171" viewBox="0 0 150 171"><rect width="150" height="171" fill="#e4eef0"/><g fill="#7eabb8"><rect x="20" y="18" width="110" height="8"/><rect x="20" y="38" width="110" height="8"/><rect x="20" y="58" width="110" height="8"/><rect x="20" y="78" width="110" height="8"/><rect x="20" y="98" width="110" height="8"/><rect x="20" y="122" width="110" height="36"/></g></svg>
    <span class="abs step-text" style="right:64px;top:84px;text-align:right;line-height:30px">We analyze the works estimate price &amp;<br>Proced to Step 2</span>
    <svg class="abs" style="left:893px;top:155px" width="40" height="44" viewBox="0 0 40 44"><path d="M20 2 V38 M6 24 L20 40 L34 24" stroke="#222" stroke-width="5" fill="none"/></svg>
  </div>
  <div class="step" style="top:335px;height:47px"><span class="step-label" style="top:9px;left:40px">Step 2</span></div>
  <div class="step" style="top:406px;height:47px"><span class="step-label" style="top:9px;left:40px">Step 3</span></div>
</section>

<section class="works">
  <h2 class="section-title">Our Latest Works</h2>
  <span class="filter" style="left:234px">All</span>
  <span class="filter active" style="left:289px">Banners</span>
  <span class="filter" style="left:408px">Flages &amp; Posters</span>
  <span class="filter" style="left:613px">Pull up Banners</span>
  <span class="filter" style="left:821px">Boards &amp; Signs</span>
  <div class="work" role="img" aria-label="Chalet in snowy mountains at night" style="left:74px;background:linear-gradient(180deg,#7f8fc9,#55639a)"></div>
  <div class="work" role="img" aria-label="Autumn forest in warm light" style="left:449px;background:linear-gradient(180deg,#c47a52,#5e2e24)"></div>
  <div class="work" role="img" aria-label="Castle under a bright sky" style="left:828px;top:178px;height:318px;background:linear-gradient(180deg,#a9bcc6,#c2aa7a 60%,#6a7448)"></div>
</section>

<section class="get-quote">
  <h2 class="section-title">Get A Quote</h2>
  <span class="field-label" style="left:78px;top:108px">Name</span>
  <span class="field-label" style="left:455px;top:112px">Phone No</span>
  <span class="field-label" style="left:829px;top:110px">Email Address</span>
  <div class="field" style="left:74px;top:138px"></div>
  <div class="field" style="left:450px;top:138px"></div>
  <div class="field" style="left:826px;top:138px"></div>
  <span class="field-label" style="left:77px;top:210px">Product Interested</span>
  <span class="field-label" style="left:453px;top:212px">Quantity</span>
  <span class="field-label" style="left:828px;top:210px">Product Code</span>
  <div class="field" style="left:74px;top:240px"></div>
  <div class="field" style="left:452px;top:240px"></div>
  <div class="field" style="left:826px;top:240px;width:298px"></div>
  <span class="field-label" style="left:78px;top:300px">Message &nbsp;&nbsp;(Please tell us your &nbsp;&nbsp;product code,color,size &nbsp;&nbsp;all info about req product)</span>
  <div class="field" style="left:74px;top:341px;width:1053px;height:135px"></div>
</section>

<section class="testimonials">
  <h2 class="section-title">Our Testimonials</h2>
  <div class="t-arrow" style="left:73px"><svg width="45" height="42" viewBox="0 0 45 42"><path d="M28 9 L16 21 L28 33" stroke="#7ea4c4" stroke-width="4" fill="none"/></svg></div>
  <div class="abs" role="img" aria-label="Couple at their wedding" style="left:149px;top:51px;width:237px;height:233px;background:linear-gradient(180deg,#a9bd8e,#e8e2da 60%,#5a5a60)"></div>
  <div class="abs" style="left:449px;top:59px;width:93px;height:30px;background:#333;color:#e8dfae;font-size:16px;text-align:center;line-height:30px;letter-spacing:2px">★★★★★</div>
  <div class="t-box" style="top:99px;height:86px;line-height:30px">“The standard Lorem Ipsum passage, used since the 1500s<br>“Lorem ipsum dolor sit a”</div>
  <div class="t-box" style="top:210px;height:51px;line-height:36px;padding-top:2px">About Authour &nbsp;&nbsp;Lorem Ipsum is a print testing text.</div>
  <div class="t-arrow" style="left:1080px"><svg width="45" height="42" viewBox="0 0 45 42"><path d="M17 9 L29 21 L17 33" stroke="#7ea4c4" stroke-width="4" fill="none"/></svg></div>
</section>

<footer class="site-footer">
  <p style="left:96px;top:24px;font-size:17px">Contact Info</p>
  <svg class="abs" style="left:100px;top:58px" width="12" height="12" viewBox="0 0 12 12"><path d="M2 1 L5 1 L6 4 L4 5 Q6 8 8 8 L9 6 L11 7 L11 10 Q4 11 1 3 Z" fill="#fff"/></svg>
  <p style="left:133px;top:56px">02 5550 1846</p>
  <svg class="abs" style="left:100px;top:92px" width="12" height="14" viewBox="0 0 12 14"><path d="M6 14 L1 6 A5 5 0 1 1 11 6 Z" fill="#fff"/><circle cx="6" cy="5" r="2" fill="#6b6b6b"/></svg>
  <p style="left:131px;top:91px">14 Kerrin Lane Marrickville Trade Park</p>
  <svg class="abs" style="left:100px;top:128px" width="14" height="11" viewBox="0 0 14 11"><rect x="1" y="1" width="12" height="9" fill="none" stroke="#d88a8a" stroke-width="1.5"/><path d="M1 1 L7 6 L13 1" stroke="#d88a8a" stroke-width="1.5" fill="none"/></svg>
  <p style="left:130px;top:126px">hello@tallowbanners.com.au</p>
  <span class="abs" style="left:267px;top:148px;width:25px;height:25px;background:#5a6e94"></span>
  <span class="abs" style="left:300px;top:148px;width:25px;height:25px;background:#5a7aa0"></span>
  <span class="abs" style="left:333px;top:148px;width:25px;height:25px;background:#b06a60"></span>
  <span class="abs" style="left:366px;top:148px;width:25px;height:25px;background:#6aa2c0"></span>
  <p style="left:610px;top:34px">Products</p>
  <p style="left:610px;top:68px">Get a Quote</p>
  <p style="left:610px;top:102px">Contact Us</p>
  <p style="left:610px;top:136px">Sitemap</p>
  <p style="left:1004px;top:36px">Terms &amp; Conditions</p>
  <p style="left:1004px;top:70px">Privacy Plicy</p>
  <p style="left:1004px;top:108px">Lorem</p>
  <p style="left:1004px;top:141px">Lorem</p>
</footer>
<div class="copyright abs" style="left:0;width:1200px">All copy rights reserved 2016</div>

</body>
</html>
```